PDN Letterhead

We need a letterhead design that will be able to be used on all marketing products (letterhead, mail chimp, envelops, business cards, etc.) We are a law firm specializing primarily in transportation law but offer a wide range of services to our clients. We would like the design to be modern, simple, and professional. Our colors are black and gold, however, we've incorporated dark gray and white on other marketing products such as our website.

```html
<!DOCTYPE html>
<html lang="en">
<head>
<meta charset="utf-8">
<title>PDN Law Group Letterhead</title>
<link href="https://fonts.googleapis.com/css2?family=Roboto:wght@400;500&display=swap" rel="stylesheet">
<style>
  :root {
    --ink: #1a1a1a;
    --muted: #444444;
    --rule: #9a9a9a;
    --paper: #ffffff;
    --backdrop: #ededed;
    --signature-tone: #d9d9d9;
  }
  * { box-sizing: border-box; margin: 0; padding: 0; }
  html, body {
    width: 1200px; height: 1200px; overflow: hidden;
    background: var(--backdrop);
    font-family: "Roboto", Arial, sans-serif;
    color: var(--ink);
  }
  .letterhead {
    position: absolute; left: 150px; top: 20px;
    width: 900px; height: 1160px;
    background: var(--paper);
  }
  .brand {
    position: absolute; left: 85px; top: 60px;
    font-weight: 400; color: var(--ink);
    letter-spacing: 4px; line-height: 1.1;
    text-align: center;
  }
  .brand-name { font-size: 54px; display: block; }
  .brand-sub { font-size: 22px; display: block; letter-spacing: 6px; }
  .contact-rules {
    position: absolute; left: 450px; top: 86px;
  }
  .contact-list {
    position: absolute; left: 472px; top: 88px;
    list-style: none;
    font-size: 10.5px; color: var(--muted);
  }
  .contact-list li {
    display: flex; align-items: center; gap: 8px;
    height: 18px;
  }
  .contact-list svg { width: 11px; height: 11px; fill: var(--ink); flex: none; }
  .salutation {
    position: absolute; left: 83px; top: 300px;
    font-size: 15px;
  }
  .letter-body {
    position: absolute; left: 83px; top: 331px; width: 736px;
    font-size: 14.6px; line-height: 18.4px;
    text-align: justify; color: var(--ink);
  }
  .letter-body p { margin-bottom: 18.4px; }
  .letter-body p.lead { text-indent: 56px; }
  .signature {
    position: absolute; left: 83px; top: 1000px;
    width: 200px; height: 68px;
    background: linear-gradient(90deg, var(--signature-tone), #f2f2f2);
  }
  .closing {
    position: absolute; left: 83px; top: 1074px;
    font-size: 15px;
  }
</style>
</head>
<body>
<main class="letterhead">
  <header>
    <div class="brand">
      <span class="brand-name">PDN</span>
      <span class="brand-sub">LAW GROUP</span>
    </div>
    <svg class="contact-rules" width="10" height="92" viewBox="0 0 10 92" aria-hidden="true">
      <line x1="2" y1="0" x2="2" y2="92" stroke="#9a9a9a" stroke-width="1"/>
      <line x1="7" y1="10" x2="7" y2="82" stroke="#1a1a1a" stroke-width="1.5"/>
    </svg>
    <ul class="contact-list">
      <li><svg viewBox="0 0 12 12"><path d="M6 0a4 4 0 0 0-4 4c0 3 4 8 4 8s4-5 4-8a4 4 0 0 0-4-4zm0 5.5A1.5 1.5 0 1 1 6 2.5a1.5 1.5 0 0 1 0 3z"/></svg>200 Harbor View Avenue, Suite 410, Coral Bay, FL 30000</li>
      <li><svg viewBox="0 0 12 12"><circle cx="6" cy="6" r="5"/></svg>555.010.2040</li>
      <li><svg viewBox="0 0 12 12"><rect x="1" y="3" width="10" height="7" rx="1"/></svg>office@pdnlawgroup.com</li>
      <li><svg viewBox="0 0 12 12"><path d="M3 1l2 2-1 2c1 2 2 3 4 4l2-1 2 2-2 2C5 12 0 7 0 3z"/></svg>555.010.2040</li>
      <li><svg viewBox="0 0 12 12"><circle cx="6" cy="6" r="5"/></svg>https://www.pdnlawgroup.com</li>
    </ul>
  </header>

  <p class="salutation">Dear Sir</p>

  <section class="letter-body">
    <p class="lead">Lorem ipsum dolor sit amet, consectetur adipiscing elit. Aliquam suscipit dolor sit amet justo commodo ullamcorper. Vivamus commodo consequat tempus. Etiam magna lectus, tempus id nibh at, sodales maximus mi. Praesent sit amet tellus sit amet velit consectetur maximus. Curabitur aliquet lectus quis est elementum, vel dapibus leo vehicula. Duis varius tortor ligula, a vulputate velit pulvinar sed. Morbi consequat id mi lacinia accumsan. Cras porta leo nec eros facilisis, sed dictum nulla pellentesque. Duis porta, diam ac elementum fringilla, enim dui suscipit ipsum, eget rutrum neque magna id massa. Nullam aliquet nisi at semper dictum. Maecenas at luctus ipsum. Ut egestas, nulla a ultricies maximus, tellus diam placerat ex, eget venenatis purus magna a enim. Ut non dui nec ante consequat lobortis at at ipsum. Quisque vel congue felis, vitae molestie orci. Duis quis quam convallis, pulvinar sapien a, pulvinar eros.</p>
    <p>Proin malesuada ut enim et dapibus. Duis enim nunc, accumsan eu augue nec, scelerisque auctor quam. Aliquam nulla lacus, interdum sit amet dui vitae, aliquet dignissim diam. Vestibulum ante ipsum primis in faucibus orci luctus et ultrices posuere cubilia Curae; Maecenas mollis tempus ligula, et viverra augue maximus ut. Praesent luctus fermentum tortor. Fusce leo erat, placerat vel eros a, sollicitudin feugiat nisl. Etiam sed ante velit. Sed vitae ultricies risus. Quisque convallis bibendum consectetur. Suspendisse non volutpat sem. Suspendisse scelerisque urna sed rutrum vulputate. Fusce non cursus eros, sit amet interdum elit. Sed id nibh diam. Vestibulum at augue egestas, molestie mauris in, ullamcorper velit.</p>
    <p>Nulla vel consequat arcu. Praesent sit amet mattis lectus. Praesent sit amet accumsan nibh. Aenean efficitur nisi ligula, non molestie felis tristique in. Praesent mollis purus non congue aliquet. Maecenas euismod justo massa. In eget dignissim mauris. Nulla a lorem vel elit auctor rutrum at non nisl.</p>
    <p>Mauris auctor fringilla metus, vel eleifend dolor tempus non. Maecenas dapibus ultrices orci quis cursus. Suspendisse potenti. Nulla eleifend magna lacus, et cursus nulla rutrum in. Quisque viverra nulla rutrum molestie lobortis. Cras condimentum est et ultricies efficitur. Curabitur eu diam orci. Morbi fermentum enim nibh, sed rutrum mi dapibus at. Aenean ante ipsum, tristique vitae lacus ut, sagittis consectetur justo. Vivamus ante purus, gravida ut ultrices sed, porta sit amet metus.</p>
    <p>Mauris non neque orci. Donec a nisl libero. Vivamus iaculis nibh eu mauris mattis, a sagittis eros</p>
  </section>

  <div class="signature" role="img" aria-label="Handwritten signature"></div>
  <p class="closing">Regards</p>
</main>
</body>
</html>
```